KT Appraisals BV business cards (a financial services company)

I am looking for a business card design that stands out in the financial advisory field of business & intellectual property valuation. The business card design should be conservative, yet different. Address details have changed since the attached business card. New address is:

Dorpelstraat 27
4817 KM Leiden
The Netherlands

Telephone number remains the same.

```html
<!DOCTYPE html>
<html lang="en">
<head>
<meta charset="utf-8">
<title>KT Appraisals BV – Business Cards</title>
<link href="https://fonts.googleapis.com/css2?family=Roboto:wght@400;700&display=swap" rel="stylesheet">
<style>
  :root {
    --backdrop: #e8e5e1;
    --card: #ffffff;
    --ink: #7a7a7a;
    --ink-strong: #767676;
    --shadow: rgba(0, 0, 0, 0.28);
  }
  * { margin: 0; padding: 0; box-sizing: border-box; }
  html, body {
    width: 1200px;
    height: 1200px;
    overflow: hidden;
    background: var(--backdrop);
    font-family: "Roboto", Arial, sans-serif;
    color: var(--ink);
  }
  .stage { position: relative; width: 1200px; height: 1200px; }
  .card {
    position: absolute;
    background: var(--card);
    border-radius: 38px;
    box-shadow: 0 6px 14px var(--shadow);
    overflow: hidden;
  }
  .card--front { left: 196px; top: 96px; width: 810px; height: 462px; }
  .card--back { left: 193px; top: 604px; width: 816px; height: 466px; }

  .brand-name {
    position: absolute;
    display: flex;
    align-items: center;
    gap: 16px;
    font-weight: 400;
    color: var(--ink);
    white-space: nowrap;
  }
  .brand-name__mark {
    display: block;
    background: var(--ink);
  }
  .card--front .brand-name {
    left: 0; right: 0; top: 196px;
    justify-content: center;
    font-size: 52px;
    letter-spacing: 1px;
  }
  .card--front .brand-name__mark { width: 34px; height: 34px; }
  .card--back .brand-name {
    left: 42px; top: 110px;
    font-size: 34px;
    letter-spacing: 0.5px;
  }
  .card--back .brand-name__mark { width: 24px; height: 24px; }

  .person__bar {
    position: absolute;
    left: 0; top: 311px;
    width: 27px; height: 44px;
    background: var(--ink);
  }
  .person {
    position: absolute;
    left: 38px; top: 310px;
    line-height: 1.2;
  }
  .person__name {
    font-size: 25px;
    font-weight: 700;
    color: var(--ink-strong);
    letter-spacing: -0.3px;
  }
  .person__credentials {
    font-size: 19px;
    font-weight: 400;
  }
  .person__role { font-size: 18px; margin-top: 2px; }

  .contact {
    position: absolute;
    right: 46px; top: 308px;
    text-align: right;
    font-size: 19px;
    line-height: 26.5px;
  }
  .contact__line { display: flex; justify-content: flex-end; align-items: center; gap: 10px; }
  .contact__icon { width: 17px; height: 17px; flex: none; }
  .address {
    position: absolute;
    right: 46px; top: 404px;
    text-align: right;
    font-size: 19px;
    line-height: 22px;
  }
</style>
</head>
<body>
<main class="stage">

  <section class="card card--front" aria-label="Card front">
    <div class="brand-name">
      <span class="brand-name__mark" aria-hidden="true"></span>
      <span>KT Appraisals BV</span>
    </div>
  </section>

  <section class="card card--back" aria-label="Card back">
    <div class="brand-name">
      <span class="brand-name__mark" aria-hidden="true"></span>
      <span>KT Appraisals BV</span>
    </div>

    <span class="person__bar" aria-hidden="true"></span>
    <div class="person">
      <p class="person__name">DANIEL VERHOEF <span class="person__credentials">CFA, ASA, RV</span></p>
      <p class="person__role">Managing Director</p>
    </div>

    <div class="contact">
      <p class="contact__line">+31 (0)70 555 0142
        <svg class="contact__icon" viewBox="0 0 24 24" aria-hidden="true"><path fill="none" stroke="currentColor" stroke-width="2" d="M6 3l3 4-2 2c1 3 4 6 7 7l2-2 4 3-2 3C11 20 4 13 3 5z"/></svg>
      </p>
      <p class="contact__line">dverhoef@ktappraisals.com
        <svg class="contact__icon" viewBox="0 0 24 24" aria-hidden="true"><rect x="3" y="6" width="18" height="13" fill="none" stroke="currentColor" stroke-width="2"/><path d="M3 6l9 7 9-7" fill="none" stroke="currentColor" stroke-width="2"/></svg>
      </p>
      <p class="contact__line">www.ktappraisals.com
        <svg class="contact__icon" viewBox="0 0 24 24" aria-hidden="true"><g fill="none" stroke="currentColor" stroke-width="1.8"><circle cx="12" cy="12" r="9"/><ellipse cx="12" cy="12" rx="4" ry="9"/><path d="M3 12h18M5 7h14M5 17h14"/></g></svg>
      </p>
    </div>

    <address class="address" style="font-style:normal">
      Dorpelstraat 27 4817 KM Leiden<br>
      The Netherlands
    </address>
  </section>

</main>
</body>
</html>
```